Need simple and modern looking business card with all my information on one side and logo on the other side
Info :
Company name - VELMAR CONSTRUCTION LLC
Company addres- 418 harbor 87th. Dunmoor park ny 10352
Email- velmarllc@tridomail.Com
Company phone number 555-318-6094
Cell number- 555-742-0583
Web site - velmarllc.Com
My name Gerald tomasino

Target Market(s)

Construction , home improvement, remodeling

Industry/Entity Type

Construction

Contact Information for Business Card

It has to be moder but at the same time simple

Font styles to use
Sans Serif

Colors
0255a3
ffffff
000000
f78f20
b1b1b1
9d9d9d
1b1b1b
33a6d7
ec1f27

Requirements
Must have
• My logo on one side maybe with a some kind of background on the other side all my information
Nice to have
• Some kind of background pictures provided by you .PLEASE HAVE ACCOUNT WITH PIXELVAULT WILL NOT PAY ANY EXTRA FEES .
Should not have
• Any kind of hamer, nails,screws, helmets itp. Please do not copy the other designs come up with something new.

```html
<!DOCTYPE html>
<html lang="en">
<head>
<meta charset="utf-8">
<title>Velmar Construction LLC — Business Card</title>
<link rel="stylesheet" href="https://fonts.googleapis.com/css2?family=Questrial&family=Open+Sans:wght@500&family=Roboto:wght@400&display=swap">
<style>
  :root {
    --brand-blue: #0b55a3;
    --mid-blue: #0a4c96;
    --deep-blue: #0a4488;
    --darker-blue: #083a78;
    --darkest-blue: #072f66;
    --title-blue: #1b55b5;
    --ink: #1b1b1b;
    --paper: #ffffff;
    --watermark: #e8e9ea;
    --stage: #ececef;
    --cell-line: rgba(255,255,255,0.18);
  }
  * { box-sizing: border-box; margin: 0; padding: 0; }
  html, body { width: 1200px; height: 1200px; overflow: hidden; }
  body { background: var(--stage); position: relative; }

  .card {
    position: absolute;
    left: 184px;
    width: 790px;
    height: 454px;
    border-radius: 48px;
    overflow: hidden;
  }
  .card--front { top: 130px; background: var(--brand-blue); }
  .card--back { top: 623px; background: var(--paper); }

  .front-arcs { position: absolute; inset: 0; }

  .wordmark {
    position: absolute;
    font-family: "Questrial", sans-serif;
    font-weight: 400;
    text-align: center;
    line-height: 1;
  }
  .wordmark__name { display: block; letter-spacing: 2px; }
  .wordmark__sub { display: block; letter-spacing: 2px; }

  .card--front .wordmark {
    left: 200px; top: 205px; width: 370px; color: var(--paper);
  }
  .card--front .wordmark__name { font-size: 84px; }
  .card--front .wordmark__sub { font-size: 26px; margin-top: 8px; }

  .card--back .wordmark {
    left: 440px; top: 122px; width: 296px; color: var(--ink);
  }
  .card--back .wordmark__name { font-size: 66px; }
  .card--back .wordmark__sub { font-size: 21px; margin-top: 6px; }

  .back-watermark {
    position: absolute;
    left: 470px; top: 300px;
    font-family: "Questrial", sans-serif;
    font-size: 96px;
    line-height: 1;
    letter-spacing: 2px;
    color: var(--watermark);
    white-space: nowrap;
  }

  .band-left {
    position: absolute; left: 0; top: 0; bottom: 0; width: 50px;
    background: var(--brand-blue);
  }
  .band-right {
    position: absolute; right: 0; top: 0; bottom: 0; width: 22px;
    background: var(--brand-blue);
  }

  .holder { position: absolute; left: 110px; top: 92px; }
  .holder__name {
    font-family: "Questrial", sans-serif;
    font-size: 32px; color: var(--ink); letter-spacing: -0.3px;
  }
  .holder__title {
    font-family: "Open Sans", sans-serif;
    font-weight: 500; font-size: 16px; color: var(--title-blue);
    margin-top: 2px;
  }

  .contact-list { position: absolute; left: 0; top: 226px; list-style: none; }
  .contact-list__item {
    display: flex; align-items: center; height: 37px;
  }
  .contact-list__icon {
    width: 50px; height: 36px; display: flex; align-items: center; justify-content: center;
    background: var(--deep-blue);
    border-bottom: 1px solid var(--cell-line);
  }
  .contact-list__icon svg { width: 22px; height: 22px; }
  .contact-list__text {
    font-family: "Roboto", sans-serif;
    font-weight: 400;
    font-size: 22px; color: var(--ink); margin-left: 6px; white-space: nowrap;
  }
</style>
</head>
<body>

<section class="card card--front" aria-label="Card front">
  <svg class="front-arcs" viewBox="0 0 790 454" preserveAspectRatio="none" aria-hidden="true">
    <circle cx="-400" cy="-100" r="805" fill="var(--mid-blue)"/>
    <circle cx="-60" cy="-150" r="470" fill="var(--deep-blue)"/>
    <path d="M616 0 Q690 210 688 454 L790 454 L790 0 Z" fill="var(--darker-blue)"/>
    <path d="M684 0 Q748 200 744 454 L790 454 L790 0 Z" fill="var(--darkest-blue)"/>
  </svg>
  <div class="wordmark">
    <span class="wordmark__name">VELMAR</span>
    <span class="wordmark__sub">CONSTRUCTION LLC</span>
  </div>
</section>

<section class="card card--back" aria-label="Card back">
  <div class="back-watermark" aria-hidden="true">VELMAR</div>

  <div class="band-left"></div>
  <div class="band-right"></div>

  <div class="holder">
    <p class="holder__name">Gerald tomasino</p>
    <p class="holder__title">Managing Director</p>
  </div>

  <div class="wordmark">
    <span class="wordmark__name">VELMAR</span>
    <span class="wordmark__sub">CONSTRUCTION LLC</span>
  </div>

  <ul class="contact-list">
    <li class="contact-list__item">
      <span class="contact-list__icon">
        <svg viewBox="0 0 24 24" fill="none" stroke="#fff" stroke-width="1.6"><circle cx="12" cy="12" r="10"/><path d="M12 18s-4-4.5-4-7.5a4 4 0 0 1 8 0C16 13.5 12 18 12 18z"/><circle cx="12" cy="10.5" r="1.4"/></svg>
      </span>
      <span class="contact-list__text">418 harbor 87th. Dunmoor park ny 10352</span>
    </li>
    <li class="contact-list__item">
      <span class="contact-list__icon">
        <svg viewBox="0 0 24 24" fill="none" stroke="#fff" stroke-width="1.8"><rect x="6.5" y="2" width="11" height="20" rx="1.5"/><line x1="10.5" y1="19" x2="13.5" y2="19"/></svg>
      </span>
      <span class="contact-list__text">555-742-0583</span>
    </li>
    <li class="contact-list__item">
      <span class="contact-list__icon">
        <svg viewBox="0 0 24 24" fill="#fff"><path d="M2 9c3-4 17-4 20 0l-1 3h-4l-1-2H8l-1 2H3z"/><path d="M5 14h14l1 7H4z"/><circle cx="12" cy="17" r="2" fill="var(--deep-blue)"/></svg>
      </span>
      <span class="contact-list__text">555-318-6094</span>
    </li>
    <li class="contact-list__item">
      <span class="contact-list__icon">
        <svg viewBox="0 0 24 24" fill="none" stroke="#fff" stroke-width="1.6"><rect x="2" y="5" width="20" height="14"/><path d="M2 5l10 8 10-8M2 19l7-7M22 19l-7-7"/></svg>
      </span>
      <span class="contact-list__text">velmarllc@tridomail.Com</span>
    </li>
    <li class="contact-list__item">
      <span class="contact-list__icon">
        <svg viewBox="0 0 24 24" fill="none" stroke="#fff" stroke-width="1.4"><circle cx="12" cy="12" r="10"/><ellipse cx="12" cy="12" rx="4.5" ry="10"/><line x1="2" y1="12" x2="22" y2="12"/><path d="M4 7h16M4 17h16"/></svg>
      </span>
      <span class="contact-list__text">velmarllc.Com</span>
    </li>
  </ul>
</section>

</body>
</html>
```